Marcus Lindqvist Photography needs a business card designs

I am looking for a business card with a logo clean and simple which I can use that logo on my website or on my pictures. It has to be very classy and very professional. Please look at my website at www.marcuslvqphoto.com for my signature. I'm thinking of something like that for my signature/logo. I'm still working on my website but you get an idea. I'm open to any design but not too busy graphics.

I will be printing the business card from qrivel.com.

Surprise me :)

contact me if you have any questions.

-ML

I'm receiving a lot of black background at the moment. I know my website is all black doesn't mean I want my card to be all black. Please send in with some white background as well. Thanks :)

check out some business cards that I found online. I think they are simple and look really awesome. I don't want a card that is too busy.

http://www.marcuslvqphoto.com/p270092084

Reason: Please extend the date for me. I haven't really receive any good design yet.

Printing

• -a logo that related to my first and last initial of my name "ML"
-double sided
• -I don't want my background to be all black.
-no pictures on the card

```html
<!DOCTYPE html>
<html lang="en">
<head>
<meta charset="utf-8">
<title>Marcus Lindqvist Photography — Business Cards</title>
<link href="https://fonts.googleapis.com/css2?family=Arimo:wght@400&family=EB+Garamond:ital,wght@0,400;0,600;1,400&display=swap" rel="stylesheet">
<style>
  :root {
    --brand-blue: #0b4f9b;
    --ink-grey: #6d6e71;
    --label-grey: #9a9b9e;
    --paper: #ffffff;
    --card-edge: #c9cacc;
    --canvas: #ffffff;
  }
  * { margin: 0; padding: 0; box-sizing: border-box; }
  html, body {
    width: 1200px; height: 900px; overflow: hidden;
    background: var(--canvas);
  }
  .sheet { position: relative; width: 1200px; height: 900px; }

  .card {
    position: absolute;
    width: 568px; height: 372px;
    text-align: center;
  }
  .card--front { left: 24px; top: 268px; background: var(--brand-blue); }
  .card--back-stacked { left: 610px; top: 74px; background: var(--paper); border: 1.5px solid var(--card-edge); }
  .card--back-ruled { left: 610px; top: 466px; background: var(--paper); border: 1.5px solid var(--card-edge); }

  .brand-mark {
    position: absolute; left: 50%;
    width: 84px; height: 84px; margin-left: -42px;
    border-radius: 50%;
  }
  .card--front .brand-mark { top: 96px; background: var(--paper); }
  .card--back-stacked .brand-mark,
  .card--back-ruled .brand-mark { top: 40px; background: var(--brand-blue); }

  .brand-name {
    position: absolute; left: 0; right: 0;
    font-family: "Arimo", Helvetica, Arial, sans-serif;
    font-weight: 400; font-size: 30px; letter-spacing: -0.3px;
    white-space: nowrap;
  }
  .card--front .brand-name { top: 214px; color: var(--paper); }
  .card--back-stacked .brand-name,
  .card--back-ruled .brand-name { top: 152px; color: var(--ink-grey); }

  .front-url {
    position: absolute; left: 0; right: 0; top: 326px;
    font-family: "EB Garamond", Garamond, serif;
    font-size: 18px; color: #d6e2f2;
  }

  .holder-name {
    position: absolute; left: 0; right: 0;
    font-family: "EB Garamond", Garamond, serif;
    font-weight: 600; font-size: 26px; color: var(--brand-blue);
  }
  .card--back-stacked .holder-name { top: 236px; }
  .card--back-ruled .holder-name { top: 224px; }

  .contact-list {
    position: absolute; left: 0; right: 0; top: 278px;
    font-family: "EB Garamond", Garamond, serif;
    font-size: 15px; line-height: 21px; color: var(--brand-blue);
    list-style: none;
  }
  .contact-label { font-style: italic; color: var(--label-grey); margin-right: 3px; }

  .contact-table {
    position: absolute; left: 0; top: 266px; width: 100%;
    font-family: "EB Garamond", Garamond, serif;
    font-size: 15px; line-height: 24px;
    border-collapse: collapse;
  }
  .contact-table th {
    width: 270px; padding-right: 8px;
    text-align: right; font-weight: 400; font-style: italic;
    color: var(--label-grey);
    border-right: 1px solid var(--card-edge);
  }
  .contact-table td { text-align: left; padding-left: 8px; color: var(--brand-blue); }
</style>
</head>
<body>
<main class="sheet">

  <section class="card card--front" aria-label="Card front">
    <span class="brand-mark" aria-hidden="true"></span>
    <p class="brand-name">Marcus Lindqvist Photography</p>
    <p class="front-url">marcuslvqphoto.com</p>
  </section>

  <section class="card card--back-stacked" aria-label="Card back, stacked contact layout">
    <span class="brand-mark" aria-hidden="true"></span>
    <p class="brand-name">Marcus Lindqvist Photography</p>
    <h2 class="holder-name">Marcus Lindqvist</h2>
    <ul class="contact-list">
      <li><span class="contact-label">phone</span>(555)214-7730</li>
      <li><span class="contact-label">email</span>marcus@marcuslvqphoto.com</li>
      <li><span class="contact-label">web</span>marcuslvqphoto.com</li>
    </ul>
  </section>

  <section class="card card--back-ruled" aria-label="Card back, ruled contact layout">
    <span class="brand-mark" aria-hidden="true"></span>
    <p class="brand-name">Marcus Lindqvist Photography</p>
    <h2 class="holder-name">Marcus Lindqvist</h2>
    <table class="contact-table">
      <tr><th scope="row">phone</th><td>(555)214-7730</td></tr>
      <tr><th scope="row">email</th><td>marcus@marcuslvqphoto.com</td></tr>
      <tr><th scope="row">web</th><td>marcuslvqphoto.com</td></tr>
    </table>
  </section>

</main>
</body>
</html>
```